Design of Labels for Harrowmere Dock Spirit bottle

Design bottle labels for Harrowmere Dock Spirit. There are three labels to design; a front, a back and a tamper band to be placed over the cork. The labels should be deigned to fit the bottle specified in the link below.
The Gin is an excellent high end premium brand Navy strength Gin 57% Vol. The bottle should evoke excellence and a romance of period of pride in the British Navy. Gin was drunk by officers in the Navy so a representation of the Officer Class should be made possibly through gold braid of a senior officer's sleeve, cap or lapel. The white ensign should also be prominent. Suggested colour themes are navy blues, grey, and white....although others schemes may be suitable. Pellick's Quay Brandy is a good example of the sort of thing we are looking for, although the design must not be so similar that it encroaches on Pellick's trade mark or copyrights. The period theme is 1900 to 1940
Bottle link: https://www.vessel-crate-supply.co.uk/Glass-bottles/350ml-flint-glass-bottle-Marlo.html
Target Market(s)
Gin Drinkers
Look and feel

```html
<!DOCTYPE html>
<html lang="en">
<head>
<meta charset="utf-8">
<title>Harrowmere Dock Spirit – Front Label</title>
<link rel="stylesheet" href="https://fonts.googleapis.com/css2?family=Cinzel:wght@600;700&display=swap">
<style>
  :root {
    --backdrop: #2b3650;
    --label-white: #ffffff;
    --label-mist: #d9dbe1;
    --label-slate: #8b90a1;
    --label-navy: #0e1836;
    --ink: #111111;
    --gold: #d9b56a;
    --gold-soft: #e3c88f;
    --ensign-red: #b2303b;
    --band-blue: #27377a;
  }
  * { box-sizing: border-box; margin: 0; padding: 0; }
  html, body {
    width: 1200px; height: 1200px; overflow: hidden;
    background: var(--backdrop);
  }
  .canvas {
    position: relative; width: 1200px; height: 1200px;
    background: var(--backdrop);
  }
  .front-label {
    position: absolute; left: 240px; top: 155px;
    width: 720px; height: 890px;
    background: linear-gradient(to bottom,
      var(--label-white) 0%,
      var(--label-white) 42%,
      var(--label-mist) 66%,
      var(--label-slate) 79%,
      #1d2849 89%,
      var(--label-navy) 100%);
    font-family: "Cinzel", "Times New Roman", serif;
    text-align: center;
  }
  .gold-frame {
    position: absolute; left: 54px; right: 54px; top: 50px; bottom: 57px;
    border: 3px solid var(--gold-soft);
    border-radius: 46px;
  }
  .brand-top {
    position: absolute; left: 0; right: 0; top: 180px;
    font-weight: 700; font-size: 66px; letter-spacing: 1px;
    color: var(--ink); line-height: 1;
  }
  .brand-mark {
    position: absolute; left: 50%; top: 330px;
    width: 108px; height: 108px; margin-left: -54px;
    border-radius: 50%;
    background: var(--ensign-red);
  }
  .brand-bottom {
    position: absolute; left: 0; right: 0; top: 495px;
    font-weight: 700; font-size: 52px; letter-spacing: 1px;
    color: var(--ink); line-height: 1;
  }
  .rule-star {
    position: absolute; left: 158px; top: 568px;
    width: 404px; height: 40px;
  }
  .tagline {
    position: absolute; left: 0; right: 0; top: 628px;
    font-weight: 600; font-size: 19px; letter-spacing: 2px;
    line-height: 30px; color: #2a2f3d;
  }
  .strength, .established {
    position: absolute; left: 285px; width: 150px; height: 27px;
    font-weight: 700; font-size: 15px; letter-spacing: 1px;
    line-height: 27px; color: var(--label-white);
  }
  .strength { top: 722px; background: var(--ensign-red); }
  .established { top: 756px; background: var(--band-blue); }
  .origin {
    position: absolute; left: 0; right: 0; top: 812px;
    font-weight: 700; font-size: 12px; letter-spacing: 1.5px;
    color: var(--label-white);
  }
</style>
</head>
<body>
  <main class="canvas">
    <section class="front-label" aria-label="Harrowmere Dock Spirit front label">
      <div class="gold-frame"></div>
      <h1 class="brand-top">HARROWMERE</h1>
      <div class="brand-mark"></div>
      <h2 class="brand-bottom">DOCK SPIRIT</h2>
      <svg class="rule-star" viewBox="0 0 404 40" aria-hidden="true">
        <polygon points="202,2 207.3,14.7 221,15.8 210.6,24.8 213.8,38 202,31 190.2,38 193.4,24.8 183,15.8 196.7,14.7" fill="#d9b56a"/>
        <line x1="0" y1="32" x2="404" y2="32" stroke="#111111" stroke-width="3"/>
      </svg>
      <p class="tagline">RICH HERITAGE<br>SMOOTH FLAVOUR</p>
      <div class="strength">57% VOL</div>
      <div class="established">EST 1920</div>
      <p class="origin">MADE IN ENGLAND</p>
    </section>
  </main>
</body>
</html>
```